Business Card and Stationary
BrookLamp Consutling
Professional
Peter Varsiklo
8276 Wimbrell Lane
Dublin, OH 43092
pvarsiklo@brooklampconsulting.com
brooklampconsulting.com

```html
<!DOCTYPE html>
<html lang="en">
<head>
<meta charset="utf-8">
<title>BrookLamp Consulting – Business Card</title>
<link rel="stylesheet" href="https://fonts.googleapis.com/css2?family=Open+Sans:wght@400;600;700&display=swap">
<style>
  :root {
    --backdrop: #2c2c2c;
    --card: #ffffff;
    --card-edge: #e6e6e6;
    --green: #7cc242;
    --green-light: #a5d86f;
    --ink: #3a3a3a;
    --ink-soft: #5c5c5c;
    --rule: #c9c9c9;
  }
  * { box-sizing: border-box; margin: 0; padding: 0; }
  html, body {
    width: 1200px;
    height: 780px;
    overflow: hidden;
    background: var(--backdrop);
    font-family: "Open Sans", Arial, sans-serif;
  }
  .business-card {
    position: absolute;
    left: 180px;
    top: 150px;
    width: 840px;
    height: 480px;
    background: var(--card);
    border-radius: 26px;
    overflow: hidden;
    box-shadow: 0 0 0 1px var(--card-edge);
  }
  .accent-band {
    position: absolute;
    left: 0; top: 0; bottom: 0;
    width: 34px;
    background: var(--green);
  }
  .accent-band::after {
    content: "";
    position: absolute;
    right: 6px; top: 0; bottom: 0;
    width: 3px;
    background: var(--green-light);
  }
  .brand {
    position: absolute;
    left: 70px;
    top: 300px;
    width: 250px;
    display: flex;
    align-items: center;
    gap: 10px;
  }
  .brand-square {
    width: 18px;
    height: 18px;
    background: var(--green);
    flex: none;
  }
  .brand-name {
    font-size: 22px;
    font-weight: 600;
    color: var(--ink);
    line-height: 1.15;
  }
  .divider {
    position: absolute;
    left: 345px;
    top: 90px;
    width: 1px;
    height: 300px;
    background: var(--rule);
  }
  .holder-name {
    position: absolute;
    left: 372px;
    top: 78px;
    font-size: 26px;
    font-weight: 700;
    color: var(--green);
  }
  .address {
    position: absolute;
    left: 372px;
    top: 190px;
    font-size: 17px;
    line-height: 1.4;
    color: var(--ink-soft);
    font-style: normal;
  }
  .contacts {
    position: absolute;
    left: 372px;
    top: 268px;
    list-style: none;
    font-size: 17px;
    color: var(--ink-soft);
  }
  .contacts li {
    display: flex;
    align-items: center;
    gap: 12px;
    height: 30px;
  }
  .contacts svg { width: 18px; height: 18px; flex: none; }
</style>
</head>
<body>
  <section class="business-card">
    <div class="accent-band"></div>

    <div class="brand">
      <span class="brand-square"></span>
      <span class="brand-name">BrookLamp Consulting</span>
    </div>

    <div class="divider"></div>

    <h1 class="holder-name">Peter Varsiklo</h1>

    <address class="address">
      8276 Wimbrell Lane<br>
      Dublin, OH 43092
    </address>

    <ul class="contacts">
      <li>
        <svg viewBox="0 0 18 18" aria-hidden="true">
          <path d="M4 2c1 0 2 2.5 2 3.2S4.8 6.5 4.8 7.2c0 1.2 4.2 5.6 5.8 5.6.7 0 1.1-1.3 1.8-1.3S16 12.6 16 13.6 14.6 16 13.2 16C8 16 2 10 2 4.8 2 3.4 3 2 4 2z" fill="var(--green)"/>
        </svg>
        <span>614-555-0187</span>
      </li>
      <li>
        <svg viewBox="0 0 18 18" aria-hidden="true">
          <circle cx="9" cy="9" r="8.5" fill="var(--green)"/>
          <rect x="4.5" y="6" width="9" height="6.5" rx="1" fill="#fff"/>
          <path d="M4.8 6.4 9 9.6l4.2-3.2" stroke="var(--green)" stroke-width="1.1" fill="none"/>
        </svg>
        <span>pvarsiklo@brooklampconsulting.com</span>
      </li>
      <li>
        <svg viewBox="0 0 18 18" aria-hidden="true">
          <circle cx="9" cy="9" r="8.5" fill="var(--green-light)"/>
          <circle cx="9" cy="9" r="4.8" fill="none" stroke="#fff" stroke-width="1.1"/>
          <path d="M4.2 9h9.6M9 4.2c2 2.6 2 7 0 9.6M9 4.2c-2 2.6-2 7 0 9.6" stroke="#fff" stroke-width="1" fill="none"/>
        </svg>
        <span>brooklampconsulting.com</span>
      </li>
    </ul>
  </section>
</body>
</html>
```